Sleek business card design for digital agency.

Brief document attached for detailed description and inspiration. Looking for a minimalist sleek, cool, modern business card design.

Industry/Entity Type

Digital

```html
<!DOCTYPE html>
<html lang="en">
<head>
<meta charset="utf-8">
<title>Harbor Kiln — Business Card</title>
<link rel="stylesheet" href="https://fonts.googleapis.com/css2?family=Open+Sans:wght@300;400;600&display=swap">
<style>
  :root {
    --stage: #2b2622;
    --card: #0a0a0b;
    --brand-grey: #5e5e5e;
    --accent-blue: #5662ab;
    --ink: #f4f4f4;
    --ink-soft: #d9d9d9;
  }
  * { box-sizing: border-box; margin: 0; padding: 0; }
  html, body {
    width: 1200px;
    height: 1200px;
    overflow: hidden;
    background: var(--stage);
    font-family: "Open Sans", Arial, sans-serif;
  }
  .canvas {
    position: relative;
    width: 1200px;
    height: 1200px;
    display: flex;
    flex-direction: column;
    align-items: center;
    justify-content: center;
    gap: 56px;
  }
  .card {
    position: relative;
    width: 900px;
    height: 514px;
    background: var(--card);
    border-radius: 22px;
    box-shadow: 0 18px 40px rgba(0,0,0,0.45);
    overflow: hidden;
  }

  /* Back of card: brand wordmark */
  .card-back {
    display: flex;
    align-items: center;
    justify-content: center;
    gap: 34px;
  }
  .brand-dot {
    width: 120px;
    height: 120px;
    border-radius: 50%;
    background: var(--brand-grey);
  }
  .brand-name {
    color: var(--brand-grey);
    font-weight: 600;
    font-size: 112px;
    letter-spacing: -1px;
    line-height: 1;
  }

  /* Front of card: contact details */
  .card-front { color: var(--ink); }
  .front-mark {
    position: absolute;
    left: 56px;
    top: 52px;
    width: 150px;
    height: 150px;
    border-radius: 50%;
    background: var(--accent-blue);
  }
  .identity {
    position: absolute;
    left: 236px;
    top: 48px;
  }
  .person-name {
    font-weight: 400;
    font-size: 74px;
    line-height: 1.05;
    letter-spacing: 2px;
  }
  .person-role {
    font-weight: 300;
    font-size: 40px;
    line-height: 1.15;
    margin-left: 60px;
    letter-spacing: 0.5px;
  }
  .person-note {
    font-size: 19px;
    margin-left: 60px;
    color: var(--ink-soft);
    letter-spacing: 0.3px;
  }
  .contact {
    position: absolute;
    bottom: 56px;
    font-weight: 400;
    color: var(--ink);
    list-style: none;
  }
  .contact-postal {
    left: 56px;
    font-size: 27px;
    line-height: 1.3;
  }
  .contact-online {
    left: 470px;
    font-size: 28px;
    line-height: 1.75;
  }
  .contact-online .handle { font-size: 36px; letter-spacing: 1px; }
</style>
</head>
<body>
<main class="canvas">
  <section class="card card-back" aria-label="Card back">
    <span class="brand-dot" aria-hidden="true"></span>
    <span class="brand-name">Harbor Kiln</span>
  </section>

  <section class="card card-front" aria-label="Card front">
    <span class="front-mark" aria-hidden="true"></span>
    <div class="identity">
      <h1 class="person-name">Daniel Ashby</h1>
      <p class="person-role">Marketing Director</p>
      <p class="person-note">Drink order: G&amp;T with cucumber</p>
    </div>
    <ul class="contact contact-postal">
      <li>Level 2, 18 Carrow Lane</li>
      <li>Eastfield NSW 2999</li>
      <li>0400 555 128</li>
      <li>03 5550 1742</li>
    </ul>
    <ul class="contact contact-online">
      <li>dashby@harborkiln.com</li>
      <li class="handle">@dashby78</li>
      <li>friendsbook.net/HarborKiln</li>
    </ul>
  </section>
</main>
</body>
</html>
```